Navigate the Underground Car Park to 7K2M Vet Clinic

Eye-catching signage for Underground Carpark.
We want to help new Clients, or those with bad senses of direction, to the correct Lift Lobby.
We want to be able to say 'Just follow the signs'.

It can be confusing and many other business have utilised some of the pillars in the carpark to guide their customers to the right place.

People don't want to walk far with sick animals so it is important they get to the right Lift Lobby.

We are thinking instead of 'Just Follow the Signs,We would like to try:'Looking for us?' (Large Text)'Follow the Signs (much smaller Text)Also, it is very useful to see the proposed sign dropped on to the photo of the car park pillars I included.Many thanks Added Friday, June 16, 2017

Target Market(s)

Customers, coming for the 1st time, trying to navigate the Underground CarPark towards the appropriate Lift lobby

Industry/Entity Type

Veterinary

Font styles to use
Serif

Colors
f78f20
00a990
0455a3

Requirements
Must have
• Logo.
• Bright. Clear. Not too cluttered.
• Warmth. Humour. Approachable.
• Please include: Building 4, Mezzanine Level
Nice to have
• Please look at our FB pages and Instagram page @7k2mvetclinic for a good feel of who we are.
• Some level of style or image continuity with the Paws For Thought Poster (see attached file)
Should not have
• Not have a medical feel

```html
<!DOCTYPE html>
<html lang="en">
<head>
<meta charset="utf-8">
<title>7K2M Vet Clinic – Car Park Sign</title>
<link rel="stylesheet" href="https://fonts.googleapis.com/css2?family=Nunito:wght@800;900&family=Arimo:wght@700&display=swap">
<style>
  :root {
    --orange: #f78f20;
    --teal: #00a990;
    --blue: #0455a3;
    --white: #ffffff;
    --backdrop: #b7c1d0;
    --dog-tan: #c98a4a;
    --dog-light: #e8c18f;
    --pattern-peach: #f6e3cc;
    --pattern-mint: #dcebe4;
  }
  html, body {
    margin: 0;
    padding: 0;
    width: 1200px;
    height: 1200px;
    overflow: hidden;
    background: var(--backdrop);
  }
  .poster {
    position: absolute;
    left: 190px;
    top: 20px;
    width: 820px;
    height: 1160px;
    background: var(--white);
    overflow: hidden;
    font-family: "Nunito", sans-serif;
  }
  .dog-pattern {
    position: absolute;
    left: 0;
    top: 500px;
    width: 820px;
    height: 660px;
    background: linear-gradient(90deg, var(--pattern-peach), var(--pattern-mint));
    opacity: 0.55;
  }
  .dog-photo {
    position: absolute;
    left: 90px;
    top: 90px;
    width: 220px;
    height: 230px;
    border-radius: 46% 46% 18px 18px;
    background: radial-gradient(circle at 50% 40%, var(--dog-light), var(--dog-tan));
    z-index: 3;
  }
  .logo {
    position: absolute;
    left: 380px;
    top: 200px;
    display: flex;
    align-items: center;
    gap: 14px;
  }
  .logo-mark {
    width: 50px;
    height: 50px;
    border-radius: 50%;
    border: 5px solid var(--teal);
    box-sizing: border-box;
    flex: none;
  }
  .logo-name {
    font-weight: 800;
    font-size: 34px;
    color: var(--orange);
    white-space: nowrap;
  }
  .headline-frame {
    position: absolute;
    left: 40px;
    top: 300px;
    width: 740px;
    height: 200px;
    border: 6px solid var(--orange);
    border-radius: 20px;
    box-sizing: border-box;
    text-align: center;
    background: var(--white);
    z-index: 2;
  }
  .headline {
    margin: 30px 0 0;
    font-weight: 900;
    font-size: 66px;
    line-height: 1;
    color: var(--orange);
    letter-spacing: 1px;
  }
  .subline {
    margin: 8px 0 0;
    font-weight: 800;
    font-size: 34px;
    line-height: 1.1;
    letter-spacing: 9px;
    color: var(--teal);
  }
  .location-badge {
    position: absolute;
    left: 320px;
    top: 468px;
    width: 190px;
    height: 190px;
    border-radius: 50%;
    background: var(--orange);
    box-shadow: 0 0 0 4px var(--white), 0 0 0 7px var(--orange);
    color: var(--white);
    font-weight: 900;
    font-size: 26px;
    line-height: 1.15;
    letter-spacing: 1px;
    display: flex;
    align-items: center;
    justify-content: center;
    text-align: center;
    z-index: 4;
  }
  .car-icon {
    position: absolute;
    left: 110px;
    top: 550px;
    width: 170px;
    height: 130px;
    z-index: 3;
  }
  .parking-sign {
    position: absolute;
    left: 55px;
    top: 680px;
    width: 730px;
    height: 450px;
    z-index: 3;
  }
  .parking-p {
    font-family: "Arimo", sans-serif;
    font-weight: 700;
    font-size: 430px;
    fill: var(--white);
  }
  .parking-word {
    font-family: "Arimo", sans-serif;
    font-weight: 700;
    font-size: 84px;
    fill: var(--white);
  }
</style>
</head>
<body>
  <main class="poster">
    <div class="dog-pattern" role="img" aria-label="Faint repeating pattern of stylised dogs in peach and mint"></div>

    <div class="dog-photo" role="img" aria-label="Photo of a smiling ginger dog peeking over the headline frame with its paws"></div>

    <div class="logo">
      <span class="logo-mark"></span>
      <span class="logo-name">7K2M Vet Clinic</span>
    </div>

    <section class="headline-frame">
      <h1 class="headline">LOOKING FOR US?</h1>
      <p class="subline">Follow the Signs</p>
    </section>

    <div class="location-badge">Building 4,<br>Mezzanine<br>Level</div>

    <svg class="car-icon" viewBox="0 0 170 130" aria-hidden="true">
      <path d="M30 50 L48 12 Q52 4 62 4 L108 4 Q118 4 122 12 L140 50 L156 46 Q164 46 164 54 L150 60 L156 70 L156 110 Q156 118 148 118 L136 118 Q128 118 128 110 L128 104 L42 104 L42 110 Q42 118 34 118 L22 118 Q14 118 14 110 L14 70 L20 60 L6 54 Q6 46 14 46 Z" fill="var(--blue)"/>
      <path d="M46 48 L58 18 Q60 14 66 14 L104 14 Q110 14 112 18 L124 48 Z" fill="var(--white)"/>
      <ellipse cx="38" cy="72" rx="14" ry="7" fill="var(--white)"/>
      <ellipse cx="132" cy="72" rx="14" ry="7" fill="var(--white)"/>
      <rect x="58" y="64" width="54" height="26" rx="6" fill="var(--white)"/>
      <g stroke="var(--blue)" stroke-width="3">
        <line x1="66" y1="68" x2="66" y2="86"/>
        <line x1="74" y1="68" x2="74" y2="86"/>
        <line x1="82" y1="68" x2="82" y2="86"/>
        <line x1="90" y1="68" x2="90" y2="86"/>
        <line x1="98" y1="68" x2="98" y2="86"/>
        <line x1="106" y1="68" x2="106" y2="86"/>
      </g>
    </svg>

    <svg class="parking-sign" viewBox="0 0 730 450" role="img" aria-label="Parking this way">
      <polygon points="0,0 570,0 730,225 570,450 0,450" fill="var(--blue)"/>
      <polygon points="470,30 565,30 705,225 565,420 470,420 610,225" fill="var(--white)"/>
      <text class="parking-p" x="20" y="390">P</text>
      <text class="parking-word" x="160" y="415">arking</text>
    </svg>
  </main>
</body>
</html>
```